KRV Flyer

Purpose: Will be an insert into Vantor Brook folder (picture of folder attached) given to clients who have purchased a residential or commercial access gate. Customers will be high end so the piece needs to speak to a high end customer (affluent). The goal is to give courtesy three month service call with the ultimate goal to secure a service contact. Pricing will vary by gate and gate traffic, so do not want to list pricing. Word Doc - V3 3 Month Courtesy Check Up has copy for flyer with suggestions for image placement.

```html
<!DOCTYPE html>
<html lang="en">
<head>
<meta charset="utf-8">
<title>Vantor Brook – 3 Month Courtesy Check-Up</title>
<link rel="stylesheet" href="https://fonts.googleapis.com/css2?family=Montserrat:wght@300;400;500;600;700;800;900&display=swap">
<style>
  :root {
    --wine: #7d1416;
    --charcoal: #3d3d3f;
    --dark-panel: #444446;
    --ink: #3a3a3c;
    --white: #ffffff;
    --black: #111111;
    --light-band: #e4e2e2;
    --backdrop: #a9a5a5;
    --photo-sky: #c9d3da;
    --photo-house: #dcd8d0;
    --photo-paving: #e7e2d8;
    --photo-steel: #8e9296;
  }
  * { box-sizing: border-box; margin: 0; padding: 0; }
  html, body { width: 899px; height: 1200px; overflow: hidden; background: var(--backdrop); }
  body { font-family: "Montserrat", sans-serif; color: var(--ink); position: relative; }

  .sheet-slot { position: absolute; top: 317px; width: 438px; height: 565px; overflow: hidden; }
  .slot-front { left: 8px; }
  .slot-back { left: 453px; }
  .page {
    position: relative; width: 730px; height: 942px; background: var(--white);
    transform: scale(0.6); transform-origin: 0 0; overflow: hidden;
  }

  /* shared tick lists */
  .ticks { list-style: none; }
  .ticks > li { position: relative; padding-left: 17px; }
  .ticks > li::before {
    content: ""; position: absolute; left: 1px; top: 3px; width: 8px; height: 4px;
    border-left: 2.2px solid var(--tick, var(--white)); border-bottom: 2.2px solid var(--tick, var(--white));
    transform: rotate(-45deg);
  }

  /* ---------- front ---------- */
  .hero-photo {
    position: absolute; left: 0; top: 0; width: 730px; height: 545px;
    background:
      linear-gradient(to bottom, rgba(255,255,255,0) 0%, rgba(255,255,255,0) 66%, rgba(255,255,255,0.85) 86%, #fff 100%),
      linear-gradient(to bottom, var(--photo-sky) 0%, var(--photo-house) 30%, #cfcac0 45%, var(--photo-paving) 60%, #eeeae2 100%);
  }
  .brand {
    position: absolute; left: 515px; top: 318px; width: 160px;
    display: flex; flex-direction: column; align-items: center; gap: 8px;
  }
  .brand-mark { width: 40px; height: 40px; border-radius: 50%; border: 3px solid var(--wine); }
  .brand-name { font-weight: 700; font-size: 18px; color: var(--wine); }

  .headline {
    position: absolute; left: 0; width: 730px; top: 415px; text-align: center;
    font-weight: 800; line-height: 1; text-transform: uppercase;
  }
  .headline .line-one { display: block; font-size: 55px; color: var(--charcoal); }
  .headline .line-two { display: block; font-size: 58px; color: var(--wine); margin-top: 8px; margin-left: -30px; }

  .intro { position: absolute; left: 54px; top: 550px; width: 640px; font-size: 16px; line-height: 1.4; }
  .intro strong { color: var(--wine); font-weight: 600; }

  .service-band {
    position: absolute; left: 0; top: 637px; width: 730px; height: 40px;
    background: var(--charcoal); color: var(--white);
    display: flex; align-items: center; justify-content: center;
    font-weight: 700; font-size: 15px; text-transform: uppercase;
  }
  .maintenance {
    position: absolute; left: 0; top: 677px; width: 730px; height: 265px;
    background: var(--wine); color: var(--white); padding: 20px 44px 0 48px;
  }
  .maintenance-head { display: flex; align-items: center; gap: 14px; }
  .round-icon {
    width: 46px; height: 46px; border-radius: 50%; background: var(--white); flex: none;
    display: flex; align-items: center; justify-content: center;
  }
  .maintenance-title { font-weight: 700; font-size: 20px; }
  .reasons { display: flex; gap: 34px; margin-top: 16px; }
  .reasons .col-left { width: 292px; }
  .reasons .col-right { width: 310px; }
  .reasons li { font-size: 11.5px; line-height: 1.36; margin-bottom: 9px; }
  .reasons .sub { list-style: none; margin-top: 5px; }
  .reasons .sub li { position: relative; padding-left: 10px; margin-bottom: 3px; }
  .reasons .sub li::before {
    content: ""; position: absolute; left: 0; top: 6px; width: 4px; height: 4px; background: var(--white);
  }

  /* ---------- back ---------- */
  .plan-photo {
    position: absolute; right: 0; top: 0; width: 460px; height: 327px;
    background:
      linear-gradient(to right, #fff 0%, rgba(255,255,255,0.75) 30%, rgba(255,255,255,0) 65%),
      linear-gradient(to bottom, #d9dbdc 0%, var(--photo-steel) 45%, #b9bcbf 75%, #d4d4d2 100%);
  }
  .plan-head { position: absolute; left: 42px; top: 28px; display: flex; gap: 10px; align-items: center; }
  .plan-head .round-icon { width: 52px; height: 52px; border: 2px solid var(--wine); }
  .plan-title {
    font-weight: 900; font-size: 23px; line-height: 1.05; color: var(--wine); text-transform: uppercase;
  }
  .benefits-pill {
    position: absolute; left: 44px; top: 91px; padding: 3px 14px; border-radius: 12px;
    background: var(--wine); color: var(--white); font-weight: 700; font-size: 13px;
  }
  .benefits { position: absolute; left: 44px; top: 124px; display: flex; gap: 18px; --tick: var(--wine); }
  .benefits .ticks { width: 172px; }
  .benefits .ticks + .ticks { width: 180px; }
  .benefits li { font-size: 11.5px; line-height: 1.25; color: var(--black); font-weight: 500; margin-bottom: 9px; }

  .inspect-band {
    position: absolute; left: 0; top: 327px; width: 730px; height: 42px; background: var(--wine);
    display: flex; align-items: center; gap: 14px; padding-left: 30px; color: var(--white);
  }
  .inspect-band .round-icon { width: 46px; height: 46px; }
  .inspect-title { font-weight: 700; font-size: 19px; text-transform: uppercase; }
  .inspect {
    position: absolute; left: 0; top: 369px; width: 730px; height: 294px; background: var(--dark-panel);
    color: var(--white); padding: 30px 0 0 44px; display: flex; gap: 14px;
  }
  .inspect .ticks { width: 200px; }
  .inspect .ticks:nth-child(3) { width: 180px; }
  .inspect li { font-size: 11px; line-height: 1.22; margin-bottom: 8px; }
  .circle-photo {
    position: absolute; left: 484px; top: 433px; width: 208px; height: 208px; border-radius: 50%;
    border: 6px solid var(--wine); box-shadow: inset 0 0 0 5px var(--white);
    background: linear-gradient(to bottom, #7fa6d0 0%, #a9c3dc 40%, #5e7a4a 62%, #d8d6d0 80%, #bdbab4 100%);
  }

  .reputation {
    position: absolute; left: 0; top: 663px; width: 730px; height: 42px; background: var(--wine);
    color: var(--white); font-weight: 800; font-size: 20px;
    display: flex; align-items: center; justify-content: center;
  }
  .sectors {
    position: absolute; left: 0; top: 705px; width: 730px; height: 36px; background: var(--black);
    color: var(--white); display: flex; justify-content: space-around; align-items: center;
    font-weight: 300; font-size: 17px; padding: 0 30px;
  }
  .sectors span { display: flex; align-items: center; gap: 8px; }
  .products {
    position: absolute; left: 0; top: 741px; width: 730px; height: 29px; background: var(--light-band);
    display: flex; justify-content: center; align-items: center; gap: 8px;
    color: var(--wine); font-weight: 700; font-size: 10.5px; text-transform: uppercase;
  }
  .products i { font-style: normal; color: var(--wine); font-weight: 400; }
  .contact-line {
    position: absolute; left: 50px; top: 786px; width: 630px;
    display: flex; justify-content: space-between; font-size: 13px; color: var(--black); font-weight: 500;
  }
  .phones {
    position: absolute; left: 44px; top: 808px; width: 640px;
    display: flex; justify-content: space-between; color: var(--wine); font-weight: 700; font-size: 14.5px;
  }
  .phones span { display: flex; align-items: center; gap: 4px; }
  .back-brand {
    position: absolute; left: 40px; top: 845px; width: 130px;
    display: flex; flex-direction: column; align-items: center; gap: 6px;
  }
  .back-brand .brand-mark { width: 34px; height: 34px; }
  .back-brand .brand-name { font-size: 15px; }
  .about {
    position: absolute; left: 220px; top: 862px; width: 320px; list-style: none;
    font-size: 11px; line-height: 1.22; color: var(--black);
  }
  .about li { position: relative; padding-left: 15px; margin-bottom: 8px; }
  .about li::before { content: ""; position: absolute; left: 0; top: 4px; width: 5px; height: 5px; background: var(--wine); }
  .parent-name {
    position: absolute; left: 595px; top: 862px; width: 100px; text-align: center;
    color: var(--wine); font-weight: 800; font-size: 34px;
  }
</style>
</head>
<body>
  <div class="sheet-slot slot-front">
    <main class="page front">
      <div class="hero-photo" role="img" aria-label="Photo of a modern white villa with a white horizontal-slat aluminum sliding gate and a gate post on a pale stone driveway"></div>
      <div class="brand"><span class="brand-mark"></span><span class="brand-name">Vantor Brook</span></div>
      <h1 class="headline"><span class="line-one">3 Month Courtesy</span><span class="line-two">Check-Up</span></h1>
      <p class="intro"><strong>Vantor Brook</strong> we will send out one of our skilled service technicians at three months after installation to make sure you are 100 percent satisfied, inspect your Custom Aluminum Gate / Access System and to answer any questions.</p>
      <div class="service-band">Servicing your automated electric gate / access system is essential</div>
      <section class="maintenance">
        <div class="maintenance-head">
          <span class="round-icon">
            <svg width="26" height="26" viewBox="0 0 30 30" aria-hidden="true">
              <path d="M6 24 L18 12" stroke="#3d3d3f" stroke-width="4" stroke-linecap="round"/>
              <circle cx="21" cy="9" r="5" fill="none" stroke="#3d3d3f" stroke-width="3"/>
              <path d="M8 7 L23 22" stroke="#3d3d3f" stroke-width="3" stroke-linecap="round"/>
            </svg>
          </span>
          <h2 class="maintenance-title">Why Preventive Maintenance?</h2>
        </div>
        <div class="reasons">
          <ul class="ticks col-left">
            <li>Automated gates are large, heavy and can be dangerous to work with. Like all mechanical systems they need regular maintenance to ensure proper operation and to prolong the life of your investment.</li>
            <li>Regular inspections often catch problems while they are small. A major overhaul or having to replace major equipment can be very expensive.</li>
          </ul>
          <ul class="ticks col-right">
            <li>A gate failure never comes at a good time, proper and regularly scheduled maintenance will help keep you from being caught stranded.</li>
            <li>Business Owners -
              <ul class="sub">
                <li>Reduce costly downtime impact.</li>
                <li>Capital repair / replacement planning.</li>
                <li>Current and future facility usage.</li>
                <li>Current and future business needs.</li>
              </ul>
            </li>
          </ul>
        </div>
      </section>
    </main>
  </div>

  <div class="sheet-slot slot-back">
    <section class="page back">
      <div class="plan-photo" role="img" aria-label="Photo of a dark slatted sliding gate with a blue gate operator motor on grey paving"></div>
      <div class="plan-head">
        <span class="round-icon">
          <svg width="26" height="28" viewBox="0 0 26 28" aria-hidden="true">
            <rect x="3" y="4" width="20" height="22" rx="2" fill="none" stroke="#3d3d3f" stroke-width="2"/>
            <rect x="9" y="1.5" width="8" height="5" rx="1" fill="#3d3d3f"/>
            <path d="M7 12h12M7 17h12M7 22h8" stroke="#3d3d3f" stroke-width="2"/>
          </svg>
        </span>
        <h2 class="plan-title">Ask about a Vantor Brook<br>planned maintenance program</h2>
      </div>
      <span class="benefits-pill">Program Benefits</span>
      <div class="benefits">
        <ul class="ticks">
          <li>Priority scheduling for service / repairs.</li>
          <li>10% discount on service calls and quoted repairs.</li>
          <li>Decrease downtime.</li>
          <li>Reduce probability of a gate or gate operator malfunction.</li>
          <li>Extend the life of your gate / access system.</li>
        </ul>
        <ul class="ticks">
          <li>Ensure the safe operation of your equipment.</li>
          <li>Decrease long term repair expense.</li>
          <li>Each service call includes a written checklist of work performed, along with recommendations for any needed repairs or product replacement.</li>
        </ul>
      </div>

      <div class="inspect-band">
        <span class="round-icon">
          <svg width="24" height="24" viewBox="0 0 30 30" aria-hidden="true">
            <path d="M6 24 L18 12" stroke="#3d3d3f" stroke-width="4" stroke-linecap="round"/>
            <circle cx="21" cy="9" r="5" fill="none" stroke="#3d3d3f" stroke-width="3"/>
          </svg>
        </span>
        <h2 class="inspect-title">What can you expect our technician to inspect?</h2>
      </div>
      <div class="inspect">
        <ul class="ticks">
          <li>Test for proper operation.</li>
          <li>Visually inspect the rollers, fasteners, brackets, and other gate hardware for proper alignment, proper tightness, and signs of damage, breakage, looseness, rust or wear.</li>
          <li>Check for secure mounting.</li>
          <li>Check all sprockets and pulleys for alignment, tighten set screws as needed.</li>
          <li>Oil or Grease bearings or chain.</li>
          <li>Moving parts lubricated.</li>
          <li>Check gear reducer oil level.</li>
        </ul>
        <ul class="ticks">
          <li>Check clutch and adjust as needed.</li>
          <li>Tighten hinges or rollers as needed.</li>
          <li>Check electrical connections.</li>
          <li>Visually inspect wiring for fraying or exposure.</li>
          <li>Test and inspect entrapment protection devices, edge sensors or photoelectric eyes.</li>
          <li>Test manual release and manual release operation.</li>
          <li>Provide detail quote for parts that require replacement.</li>
        </ul>
        <ul class="ticks">
          <li>Our Reputation Is Your Peace of Mind</li>
        </ul>
      </div>
      <div class="circle-photo" role="img" aria-label="Round photo of a dark slatted entrance gate between white pillars with palm trees"></div>

      <div class="reputation">Our Reputation Is Your Peace of Mind</div>
      <div class="sectors">
        <span><svg width="18" height="16" viewBox="0 0 18 16" aria-hidden="true"><path d="M9 1 L17 8 H14 V15 H11 V10 H7 V15 H4 V8 H1 Z" fill="#fff"/></svg>RESIDENTIAL</span>
        <span><svg width="16" height="16" viewBox="0 0 16 16" aria-hidden="true"><rect x="2" y="1" width="12" height="15" fill="#fff"/><path d="M4 3h2v2H4zM10 3h2v2h-2zM4 7h2v2H4zM10 7h2v2h-2z" fill="#111"/></svg>COMMERCIAL</span>
        <span><svg width="18" height="16" viewBox="0 0 18 16" aria-hidden="true"><path d="M1 16 V8 L6 5 V8 L11 5 V8 L14 6 V0 H16 V16 Z" fill="#fff"/></svg>INDUSTRIAL</span>
      </div>
      <div class="products">
        <span>Custom Alumimun Gates</span><i>|</i><span>Access Systems</span><i>|</i><span>Automatic Openers</span><i>|</i><span>Security Barier Arms</span>
      </div>
      <div class="contact-line">
        <span>Same Day and 24/7 Emergency Service Available</span>
        <span>Visit our website:&nbsp; krv-vb.com</span>
      </div>
      <div class="phones">
        <span><svg width="12" height="12" viewBox="0 0 12 12" aria-hidden="true"><path d="M3 1 L5 3.5 L4 5 Q5.5 7 7 8 L8.5 7 L11 9 L9.5 11 Q4 10 1 2.5 Z" fill="#7d1416"/></svg>555.014.2300</span>
        <span><svg width="12" height="12" viewBox="0 0 12 12" aria-hidden="true"><path d="M3 1 L5 3.5 L4 5 Q5.5 7 7 8 L8.5 7 L11 9 L9.5 11 Q4 10 1 2.5 Z" fill="#7d1416"/></svg>555.016.7699</span>
        <span><svg width="12" height="12" viewBox="0 0 12 12" aria-hidden="true"><path d="M3 1 L5 3.5 L4 5 Q5.5 7 7 8 L8.5 7 L11 9 L9.5 11 Q4 10 1 2.5 Z" fill="#7d1416"/></svg>555.014.7474</span>
      </div>
      <div class="back-brand"><span class="brand-mark"></span><span class="brand-name">Vantor Brook</span></div>
      <ul class="about">
        <li>Vantor Brook, a division of KRV, is a third generation family run business established in 1964.</li>
        <li>We thank all our customers for our growth and many years in business.</li>
      </ul>
      <div class="parent-name">KRV</div>
    </section>
  </div>
</body>
</html>
```